Create website for home automation - Control your lighting, fans, blinds etc remotely by smartphone

Plan for STOREVAN Website - Brightnest Dwellings
Company name: Brightnest Dwellings
Company Slogan: Calm Evenings Done Right
Clean, Modern, Easy to Navigate, easy to maintain - not a lot of coding. We need flash technology but displaying simply what we do.
What we provide:
We will be offering wireless switch which can be added to iOS/Android App via WiFi, allowing users to remotely turn on/off connected lights, fans, security cameras, appliances, irrigation, humidifier separately from anywhere at any time.
Control your home away from home. No more wandering of your mind on those lights or appliances which you might have left switched on. No need to drive back home to check and switch them off. Save that energy, money and time just with a click of your phone no matter how far you are from home.
Replace your home electrical switches with smart switches. They retrofit existing electrical switches and allow you to make the transformation as needed.
Easy to use and intuitive app allows you to control your lights and devices just at a click. Set any kind of ambiance suiting your occasion.
Set scenes in smartphone app to group and operate your devices just at a button click. Same device can be included in more than one scene.
Collections and Products
Light Switches
Wall Plugs
Fan Switch
Pendants etc special lighting types.
Light Dimmers
Blind Controllers
Home Page:
Home page needs to telling customers what we do and how we do it in a few words to grab people.
Logo
Phone
Email
Support – Download instructions per product
Client login
Wholesale login
Promotional video to be on home screen - this is a short 1.5 - 2 min illustration introduction video to who we are and what we do - this is yet to be created)
Social media link - Facebook
Pages:
FAQ
About Us
Support/Shipping/Returns policy
Support/Installation
Blog posts
Product pages:
Description
Price
Space for where a video will be featured - how each product works/installation.
Reviews
Our competition:
http://www.pvorn.com.au
https://lumalodgeguide.com.au/2018/04/05/best-smart-light-switches-and-plugs/
https://www.zentiqo.com
Attachments:
Logo
Product pics
Promotional video - if ready

```html
<!DOCTYPE html>
<html lang="en">
<head>
<meta charset="utf-8">
<title>Brightnest Dwellings — Blog</title>
<link rel="stylesheet" href="https://fonts.googleapis.com/css2?family=Montserrat:wght@300;400;500;700&display=swap">
<style>
:root{
  --brand-navy:#16318c;
  --brand-blue:#1f6fc0;
  --hero-deep:#0d4f99;
  --hero-mid:#1b78c8;
  --ink:#444;
  --ink-soft:#9a9a9a;
  --rule:#e2e2e2;
  --accent:#2bb3a3;
  --footer-bg:#262626;
  --footer-ink:#ffffff;
  --icon-blue:#1f6fc0;
  --page:#ffffff;
}
*{margin:0;padding:0;box-sizing:border-box}
html,body{width:960px;height:1200px;overflow:hidden;background:var(--page)}
body{font-family:"Montserrat",sans-serif;color:var(--ink);position:relative}

.site-header{position:absolute;left:0;top:0;width:960px;height:88px;background:var(--page)}
.brand{position:absolute;left:120px;top:26px;width:200px}
.brand-row{display:flex;align-items:center;gap:7px}
.brand-mark{width:14px;height:14px;background:var(--brand-navy)}
.brand-name{font-weight:700;font-size:13px;color:var(--brand-navy);letter-spacing:.2px}
.brand-slogan{font-size:6.5px;color:var(--brand-blue);letter-spacing:1px;margin:4px 0 0 21px}
.main-nav{position:absolute;left:0;top:34px}
.main-nav a{font-size:11.5px;color:#333;text-decoration:none;position:absolute;white-space:nowrap}

.hero{position:absolute;left:0;top:88px;width:960px;height:253px;
  background:radial-gradient(ellipse at 50% 45%,var(--hero-mid) 0%,var(--hero-deep) 75%);
  display:flex;align-items:center;justify-content:center}
.hero-title{font-weight:300;font-size:43px;color:#fff;letter-spacing:1px}

.post{position:absolute;top:404px;width:241px}
.post-photo{height:160px}
.post-title{font-size:14px;font-weight:400;color:#444;line-height:17px;margin:18px 15px 0;height:59px}
.post-excerpt{font-size:10px;font-weight:300;color:var(--ink-soft);line-height:14px;margin:0 15px;height:70px;
  overflow:hidden;display:-webkit-box;-webkit-line-clamp:5;-webkit-box-orient:vertical;letter-spacing:-.1px}
.post-rule{border:0;border-top:1px solid var(--rule);margin:6px 15px 0}
.read-more{display:block;font-size:8.5px;font-weight:400;color:#333;text-decoration:none;margin:15px 15px 0;letter-spacing:.2px}
.read-more span{color:var(--accent);margin-left:3px}

.site-footer{position:absolute;left:0;top:831px;width:960px;height:204px;background:var(--footer-bg);color:var(--footer-ink);text-align:center}
.footer-nav{position:absolute;top:38px;left:0;width:960px;display:flex;justify-content:center;gap:26px}
.footer-nav a{font-size:11.5px;color:var(--footer-ink);text-decoration:none}
.social{position:absolute;top:83px;left:394px;display:flex;gap:7px}
.social span{width:18px;height:18px;background:var(--icon-blue);border-radius:2px;display:block}
.company-details{position:absolute;top:120px;left:0;width:960px;font-size:11px;line-height:14px;font-style:normal}
</style>
</head>
<body>

<header class="site-header">
  <div class="brand">
    <div class="brand-row"><span class="brand-mark"></span><span class="brand-name">Brightnest Dwellings</span></div>
    <div class="brand-slogan">Calm Evenings Done Right</div>
  </div>
  <nav class="main-nav">
    <a href="#" style="left:411px">About Us</a>
    <a href="#" style="left:483px">Products</a>
    <a href="#" style="left:554px">Shipping</a>
    <a href="#" style="left:624px">Support</a>
    <a href="#" style="left:690px">Blog</a>
    <a href="#" style="left:740px">Contact Us</a>
    <a href="#" style="left:821px">Login</a>
  </nav>
</header>

<section class="hero" role="img" aria-label="Blue abstract network background">
  <h1 class="hero-title">BLOG</h1>
</section>

<article class="post" style="left:99px">
  <div class="post-photo" role="img" aria-label="Hand holding a smartphone showing a camera app outdoors" style="background:linear-gradient(135deg,#6f8a3e,#a9b873 55%,#5b4a3c)"></div>
  <h2 class="post-title">Owen’s clear catch</h2>
  <p class="post-excerpt">I had landed in Phoenix for a convention and decided to grab some lunch. As I was sitting at the table, I got a notification: “Person - Entryway: Your camera spotted someone.” This was a rare notification to...</p>
  <hr class="post-rule">
  <a class="read-more" href="#">READ MORE<span>›</span></a>
</article>

<article class="post" style="left:359px">
  <div class="post-photo" role="img" aria-label="Smoke detector on a ceiling above storage boxes" style="background:linear-gradient(180deg,#b9b9b9,#8f8f8f 60%,#7a5a3e)"></div>
  <h2 class="post-title">Mara’s traveling fire</h2>
  <p class="post-excerpt">We purchased two Kestra Guards for our new home. We already had the thermostat and were excited to introduce new Kestra products to the home. We bought the smoke detectors for several reasons. We...</p>
  <hr class="post-rule">
  <a class="read-more" href="#">READ MORE<span>›</span></a>
</article>

<article class="post" style="left:621px">
  <div class="post-photo" role="img" aria-label="Child in a knitted hat looking out at falling snow" style="background:linear-gradient(135deg,#4a4a4a,#9c9c9c 50%,#3b3f44)"></div>
  <h2 class="post-title">This Earth Day, help us bring energy efficiency to those who need it most</h2>
  <p class="post-excerpt">Saving energy is core to our mission of creating a home that cares for the people inside it and the world around it. That’s why this Earth Day...</p>
  <hr class="post-rule">
  <a class="read-more" href="#">READ MORE<span>›</span></a>
</article>

<footer class="site-footer">
  <nav class="footer-nav">
    <a href="#">Home</a><a href="#">About Us</a><a href="#">Products</a><a href="#">Shipping</a>
    <a href="#">Support</a><a href="#">Bog</a><a href="#">Contact Us</a><a href="#">Login</a>
  </nav>
  <div class="social" aria-label="Social links">
    <span></span><span></span><span></span><span></span><span></span><span></span><span></span>
  </div>
  <address class="company-details">
    ABN: 47 215 903 118<br>
    Office: 4/22 Marlow Lane GLENBROOK NSW 2773<br>
    Telephone: (02) 5550 1846
  </address>
</footer>

</body>
</html>
```